Business Consulting Business Card

professional business card with basic information (1) First and Last name (2) email address, (3) phone number, (4) website.

```html
<!DOCTYPE html>
<html lang="en">
<head>
<meta charset="utf-8">
<title>Tidewell Business Card</title>
<link href="https://fonts.googleapis.com/css2?family=Roboto:wght@400;500;700&display=swap" rel="stylesheet">
<style>
  :root {
    --backdrop: #d9d9db;
    --card-white: #ffffff;
    --teal: #3aa9c4;
    --teal-light: #3fb7b7;
    --teal-deep: #3d9cc6;
    --navy: #1f2a3c;
    --text-grey: #4a4f57;
    --rule-grey: #b9bcc1;
  }
  * { margin: 0; padding: 0; box-sizing: border-box; }
  html, body { width: 1200px; height: 800px; overflow: hidden; }
  body {
    background: var(--backdrop);
    font-family: "Roboto", Arial, sans-serif;
    position: relative;
  }
  .card {
    position: absolute;
    top: 246px;
    width: 540px;
    height: 308px;
    overflow: hidden;
    box-shadow: 0 6px 18px rgba(0,0,0,0.18);
  }
  .card-front { left: 40px; background: var(--card-white); }
  .card-back {
    left: 620px;
    background: linear-gradient(120deg, var(--teal-light) 0%, var(--teal-deep) 100%);
  }
  .brand {
    position: absolute;
    left: 44px;
    top: 136px;
    display: flex;
    align-items: center;
    gap: 14px;
  }
  .brand-dot {
    width: 34px; height: 34px; border-radius: 50%;
    background: var(--teal);
  }
  .brand-name {
    font-weight: 500;
    font-size: 22px;
    letter-spacing: 6px;
    color: var(--navy);
  }
  .divider {
    position: absolute;
    left: 272px; top: 60px;
    width: 1px; height: 188px;
    background: var(--rule-grey);
  }
  .contact {
    position: absolute;
    left: 292px; top: 62px;
    color: var(--text-grey);
    font-size: 12.5px;
    line-height: 1.45;
  }
  .contact-name {
    font-weight: 700;
    font-size: 21px;
    color: var(--teal);
    line-height: 1.1;
  }
  .contact-title {
    font-weight: 700;
    font-size: 13px;
    color: var(--navy);
    margin-bottom: 10px;
  }
  .contact-address { margin-bottom: 8px; }
  .contact-list { list-style: none; }
  .contact-list li { display: flex; align-items: center; gap: 8px; }
  .contact-list svg { width: 11px; height: 11px; flex: none; fill: var(--teal); }
  .edge-band {
    position: absolute; left: 0; right: 0; bottom: 0;
    height: 6px; background: var(--teal);
  }
  .back-name {
    position: absolute;
    left: 0; right: 0; top: 116px;
    text-align: center;
    font-weight: 500;
    font-size: 40px;
    letter-spacing: 10px;
    color: #ffffff;
  }
  .back-web {
    position: absolute;
    left: 0; right: 0; bottom: 44px;
    text-align: center;
    font-size: 14px;
    letter-spacing: 4px;
    color: #ffffff;
  }
</style>
</head>
<body>
  <section class="card card-front">
    <div class="brand">
      <span class="brand-dot"></span>
      <span class="brand-name">TIDEWELL</span>
    </div>
    <div class="divider"></div>
    <div class="contact">
      <div class="contact-name">Daniel Harper</div>
      <div class="contact-title">President</div>
      <div class="contact-address">4120 Birchwood Road<br>Juneau, Alaska 99801</div>
      <ul class="contact-list">
        <li><svg viewBox="0 0 12 12"><path d="M2.5 1l2 2-1 1.5c.6 1.4 1.6 2.4 3 3L8 6.5l2 2-1.5 2C4.5 10 2 7.5 1 3.5z"/></svg>555-214-7730</li>
        <li><svg viewBox="0 0 12 12"><path d="M3 1h6v10H3zM4 2v7h4V2z"/></svg>555-618-2049</li>
        <li><svg viewBox="0 0 12 12"><path d="M3 1h5v3H3zM1 5h10v6H1zM3 7v2h6V7z"/></svg>555-390-4172</li>
        <li><svg viewBox="0 0 12 12"><path d="M1 2h10v8H1zM2.5 6l1-1 1.8 1.8L8.6 3.5l1 1-4.3 4.3z"/></svg>name@tidewell.com</li>
        <li><svg viewBox="0 0 12 12"><circle cx="6" cy="6" r="5"/></svg>www.tidewell.com</li>
      </ul>
    </div>
    <div class="edge-band"></div>
  </section>

  <section class="card card-back">
    <div class="back-name">TIDEWELL</div>
    <div class="back-web">www.tidewell.com</div>
  </section>
</body>
</html>
```